Brightkeel Logistics - Cards and Logo

We need a logo and card design for a Logistics company located in Chicago. Our competitors are KTR and Qorvan. We would like to see designs that incorporate a logo that shows all ways in terms of direction. The colors would be Electric Blue, Grays, Blacks and White. I like how Moko has a badge type logo that is strong and clean. Velmora also has a strong font that is futuristic. The final design should communicate we are a strong and technological type of company. I show a picture of the colors we like from a moko cooler.

```html
<!DOCTYPE html>
<html lang="en">
<head>
<meta charset="utf-8">
<title>Brightkeel Logistics – Business Cards</title>
<link rel="stylesheet" href="https://fonts.googleapis.com/css2?family=Arimo:wght@400;700&display=swap">
<style>
  :root {
    --bg: #1c1c1c;
    --card: #0d0d0d;
    --white: #f4f4f4;
    --blue: #3a9ad9;
    --gray: #8c8c8c;
    --rule: #cfcfcf;
  }
  * { box-sizing: border-box; margin: 0; padding: 0; }
  html, body { width: 1200px; height: 1200px; overflow: hidden; }
  body {
    background: var(--bg);
    font-family: "Arimo", Arial, sans-serif;
    color: var(--white);
    display: flex;
    flex-direction: column;
    align-items: center;
    justify-content: center;
    gap: 56px;
  }
  .card {
    width: 900px;
    height: 514px;
    background: var(--card);
    border-radius: 22px;
    position: relative;
    box-shadow: 0 18px 40px rgba(0,0,0,.55);
  }
  .brand {
    display: flex;
    align-items: center;
    gap: 18px;
  }
  .brand-square {
    width: 64px;
    height: 64px;
    border-radius: 8px;
    background: var(--gray);
  }
  .brand-name {
    font-weight: 700;
    font-size: 34px;
    letter-spacing: 2px;
    text-transform: uppercase;
    color: var(--white);
    line-height: 1.1;
  }
  /* Back side */
  .card-back {
    display: flex;
    flex-direction: column;
    align-items: center;
    justify-content: center;
  }
  .card-back .brand { margin-top: 10px; }
  .card-back .site {
    margin-top: 92px;
    font-size: 20px;
    letter-spacing: .5px;
  }
  /* Front side */
  .card-front .brand {
    position: absolute;
    left: 60px;
    top: 96px;
    width: 330px;
    align-items: flex-start;
  }
  .card-front .brand-name { font-size: 30px; }
  .divider {
    position: absolute;
    left: 440px;
    top: 60px;
    bottom: 60px;
    width: 2px;
    background: var(--rule);
  }
  .details {
    position: absolute;
    left: 486px;
    top: 62px;
    bottom: 60px;
    right: 40px;
    display: flex;
    flex-direction: column;
    justify-content: space-between;
  }
  .person-name { font-weight: 700; font-size: 27px; }
  .person-role { color: var(--blue); font-size: 21px; margin-top: 4px; }
  .address { font-size: 20px; line-height: 1.35; margin-top: 14px; }
  .contact-list { list-style: none; font-size: 22px; line-height: 1.55; }
  .contact-list li { display: flex; align-items: center; gap: 16px; }
  .contact-list svg { width: 24px; height: 24px; flex: none; fill: var(--blue); }
</style>
</head>
<body>
  <section class="card card-back">
    <div class="brand">
      <div class="brand-square"></div>
      <div class="brand-name">Brightkeel Logistics</div>
    </div>
    <p class="site">www.brightkeellogistics.com</p>
  </section>

  <section class="card card-front">
    <div class="brand">
      <div class="brand-square"></div>
      <div class="brand-name">Brightkeel<br>Logistics</div>
    </div>
    <div class="divider"></div>
    <div class="details">
      <div class="identity">
        <p class="person-name">Daniel Marsh</p>
        <p class="person-role">CEO/Founder</p>
        <p class="address">208 W. Harbor Lane<br>Suite B, Elmvale<br>CA 90412</p>
      </div>
      <ul class="contact-list">
        <li>
          <svg viewBox="0 0 24 24" aria-hidden="true"><path d="M6.6 10.8a15 15 0 0 0 6.6 6.6l2.2-2.2a1 1 0 0 1 1-.25 11.4 11.4 0 0 0 3.6.57 1 1 0 0 1 1 1V20a1 1 0 0 1-1 1A17 17 0 0 1 3 4a1 1 0 0 1 1-1h3.5a1 1 0 0 1 1 1c0 1.25.2 2.45.57 3.57a1 1 0 0 1-.25 1z"/></svg>
          310.555.0147
        </li>
        <li>
          <svg viewBox="0 0 24 24" aria-hidden="true"><path d="M6 3h12v5H6zM4 9h16a2 2 0 0 1 2 2v6h-4v4H6v-4H2v-6a2 2 0 0 1 2-2zm4 6v4h8v-4z"/></svg>
          310.555.0182
        </li>
        <li>
          <svg viewBox="0 0 24 24" aria-hidden="true"><path d="M2 5h20v14H2zm2 2v.4l8 5.2 8-5.2V7zm0 2.8V17h16V9.8l-8 5.2z"/></svg>
          daniel@brightkeellogistics
        </li>
        <li>
          <svg viewBox="0 0 24 24" aria-hidden="true"><path d="M12 2a10 10 0 1 0 0 20 10 10 0 0 0 0-20zm-1 2.1V8H7.4A8 8 0 0 1 11 4.1zm2 0A8 8 0 0 1 16.6 8H13zM5 12c0-.7.1-1.4.3-2H11v4H5.3A8 8 0 0 1 5 12zm8-2h5.7a8 8 0 0 1 0 4H13zm-5.6 6H11v3.9A8 8 0 0 1 7.4 16zm5.6 0h3.6a8 8 0 0 1-3.6 3.9z"/></svg>
          www.brightkeellogistics.com
        </li>
      </ul>
    </div>
  </section>
</body>
</html>
```